Stationary pack
Stationary
Project: Stationary pack
Stationary pack - Construction
Creative Brief
Simple
Derek Olsworth
318 Harrowdene Lane Stoketon Marbury Wealdshire ME7 4RB
brightlinejoiner@mailvane.net

```html
<!DOCTYPE html>
<html lang="en">
<head>
<meta charset="utf-8">
<title>Derek Olsworth Kitchen Fitter – Business Card</title>
<link href="https://fonts.googleapis.com/css2?family=Roboto:wght@400;500&display=swap" rel="stylesheet">
<style>
  :root {
    --blue: #1f7fd0;
    --grey: #9a9a9a;
    --grey-light: #c8c8c8;
    --wave-grey: #d0d0d0;
    --ink: #555555;
    --card: #ffffff;
    --backdrop: #e9eaec;
  }
  * { margin: 0; padding: 0; box-sizing: border-box; }
  html, body { width: 1200px; height: 906px; overflow: hidden; }
  body {
    background: var(--backdrop);
    font-family: "Roboto", Arial, sans-serif;
    display: flex;
    align-items: center;
    justify-content: center;
    gap: 40px;
  }
  .card {
    position: relative;
    width: 540px;
    height: 310px;
    border-radius: 18px;
    background: var(--card);
    overflow: hidden;
    box-shadow: 0 4px 14px rgba(0,0,0,0.12);
  }
  /* front */
  .card--front {
    border: 10px solid var(--blue);
    display: flex;
    align-items: center;
    justify-content: center;
  }
  .card--front .inner-frame {
    position: absolute;
    inset: 8px;
    border: 5px solid var(--grey-light);
    border-radius: 6px;
  }
  .brand {
    display: flex;
    align-items: center;
    gap: 12px;
    color: var(--blue);
    font-weight: 500;
  }
  .brand__mark {
    background: var(--grey);
    flex: none;
  }
  .brand__name { line-height: 1.1; text-transform: uppercase; letter-spacing: 1px; }
  .brand__name span { display: block; }
  .card--front .brand__name { font-size: 24px; }
  .card--front .brand__mark { width: 56px; height: 56px; }
  /* back */
  .card--back .wave { position: absolute; inset: 0; }
  .contact {
    position: absolute;
    left: 245px;
    top: 58px;
    color: var(--ink);
  }
  .contact__name {
    color: var(--blue);
    font-size: 22px;
    font-weight: 500;
    margin-bottom: 12px;
  }
  .contact__row {
    display: flex;
    align-items: flex-start;
    gap: 8px;
    font-size: 11px;
    line-height: 1.4;
    margin-bottom: 5px;
    max-width: 200px;
  }
  .contact__row svg { flex: none; margin-top: 2px; }
  .card--back .brand {
    position: absolute;
    left: 36px;
    bottom: 40px;
  }
  .card--back .brand__name { font-size: 15px; }
  .card--back .brand__mark { width: 36px; height: 36px; }
</style>
</head>
<body>
  <section class="card card--front">
    <div class="inner-frame"></div>
    <div class="brand">
      <div class="brand__mark"></div>
      <div class="brand__name"><span>Derek Olsworth</span><span>Kitchen Fitter</span></div>
    </div>
  </section>

  <section class="card card--back">
    <svg class="wave" viewBox="0 0 540 310" preserveAspectRatio="none" aria-hidden="true">
      <path d="M470 0 C520 60 510 170 420 230 C330 290 160 300 0 290 L0 310 L540 310 L540 0 Z" fill="var(--wave-grey)"/>
      <path d="M495 0 C540 70 530 190 430 250 C330 300 160 305 0 300 L0 310 L540 310 L540 0 Z" fill="var(--card)"/>
      <path d="M505 0 C545 80 535 200 440 262 C340 310 170 310 0 306 L0 310 L540 310 L540 0 Z" fill="var(--blue)"/>
    </svg>
    <div class="contact">
      <div class="contact__name">Derek Olsworth</div>
      <div class="contact__row">
        <svg width="10" height="12" viewBox="0 0 10 12"><path d="M5 0a4 4 0 0 1 4 4c0 3-4 8-4 8S1 7 1 4a4 4 0 0 1 4-4z" fill="var(--blue)"/><circle cx="5" cy="4" r="1.5" fill="#fff"/></svg>
        <span>318 Harrowdene Lane Stoketon Marbury Wealdshire ME7 4RB</span>
      </div>
      <div class="contact__row">
        <svg width="10" height="12" viewBox="0 0 10 12"><rect x="1" y="0" width="8" height="12" rx="1.5" fill="var(--blue)"/><rect x="2.5" y="2" width="5" height="7" fill="#fff"/></svg>
        <span>07700 900318</span>
      </div>
      <div class="contact__row">
        <svg width="12" height="10" viewBox="0 0 12 10"><rect width="12" height="9" rx="1" fill="var(--blue)"/><path d="M0.5 0.8 6 5 11.5 0.8" stroke="#fff" fill="none"/></svg>
        <span>brightlinejoiner@mailvane.net</span>
      </div>
    </div>
    <div class="brand">
      <div class="brand__mark"></div>
      <div class="brand__name"><span>Derek Olsworth</span><span>Kitchen Fitter</span></div>
    </div>
  </section>
</body>
</html>
```